Bright Tooth Dentistry Business Card

We need business cards for our dental office.
We are looking for a clean, elegant design

We provide dental services to children.
Our card needs to be appealing to referring dentists, parents and our team

Target Market(s)

referring dentists, parents and our team

Industry/Entity Type

Dental Clinic

Contact Information for Business Card

4816 Juniper Lane, Suite 240
Cedar Hollow, PA 15237

412-837-2961 Voice
412-837-2962 fax
info@brighttoothdentalpa.com email
www.brighttoothdentalpa.com web

Font styles to use
Sans Serif

Requirements
Must have
• White background - clean, crisp, elegant, simple
• rounded corners
• different color palate - once we come up with design, we will replace the blue with orange, green,
Nice to have
• Follow our logo typeface and colors
• then we can replace color

```html
<!DOCTYPE html>
<html lang="en">
<head>
<meta charset="utf-8">
<title>Bright Tooth Dentistry – Business Card</title>
<link rel="stylesheet" href="https://fonts.googleapis.com/css2?family=Quicksand:wght@500;600;700&display=swap">
<style>
  :root {
    --brand-orange: #f39420;
    --text-grey: #8e8e92;
    --card-white: #ffffff;
    --backdrop: #e9e5df;
  }
  * { margin: 0; padding: 0; box-sizing: border-box; }
  html, body { width: 1189px; height: 1200px; overflow: hidden; }
  body {
    background: var(--backdrop);
    font-family: "Quicksand", sans-serif;
    position: relative;
  }
  .card {
    position: absolute;
    left: 169px;
    width: 851px;
    height: 485px;
    border-radius: 34px;
    overflow: hidden;
    text-align: center;
    box-shadow: 0 6px 14px rgba(0,0,0,0.18);
  }
  .card--front { top: 111px; background: var(--card-white); }
  .card--back { top: 640px; background: var(--brand-orange); }

  .card__band {
    position: absolute; left: 0; right: 0; bottom: 0;
    height: 11px; background: var(--brand-orange);
  }

  .brand-dot {
    position: absolute; left: 50%;
    width: 88px; height: 88px; margin-left: -44px;
    border-radius: 50%;
  }
  .card--front .brand-dot { top: 70px; background: var(--brand-orange); }
  .card--back .brand-dot { top: 172px; background: var(--card-white); }

  .brand-name {
    position: absolute; left: 0; right: 0;
    font-weight: 700; font-size: 50px; letter-spacing: -0.5px;
    line-height: 1;
  }
  .card--front .brand-name { top: 200px; color: var(--brand-orange); }
  .card--back .brand-name { top: 290px; color: var(--card-white); }

  .holder-name {
    position: absolute; left: 0; right: 0; top: 292px;
    font-weight: 600; font-size: 29px; line-height: 1.2;
    color: var(--brand-orange); letter-spacing: 0.5px;
  }
  .contact {
    position: absolute; left: 0; right: 0;
    font-weight: 600; font-size: 19px; line-height: 1.2;
    letter-spacing: 0.3px; color: var(--text-grey);
    white-space: nowrap;
  }
  .contact--address { top: 347px; }
  .contact--lines { top: 380px; }
  .contact--web { top: 409px; letter-spacing: 0.8px; }
  .label, .accent { color: var(--brand-orange); }
  .sep { margin: 0 5px; }
</style>
</head>
<body>
  <section class="card card--front">
    <div class="brand-dot"></div>
    <div class="brand-name">Bright Tooth Dentistry</div>
    <div class="holder-name">Daniel Reyes</div>
    <p class="contact contact--address">4816 Juniper Lane, Suite 240, Cedar Hollow, PA 15237</p>
    <p class="contact contact--lines">
      <span class="label">Voice:</span> 412-837-2961<span class="sep">|</span><span class="label">Fax:</span> 412-837-2962<span class="sep">|</span><span class="label">Email:</span> info@brighttoothdentalpa.com
    </p>
    <p class="contact contact--web">www.<span class="accent">brighttoothdentalpa</span>.com</p>
    <div class="card__band"></div>
  </section>

  <section class="card card--back">
    <div class="brand-dot"></div>
    <div class="brand-name">Bright Tooth Dentistry</div>
  </section>
</body>
</html>
```